Couples Workshop Flyer

I need a flyer to promote a one-day workshop for couples.

I am a therapist and life-coach and the session is called: "Lantern Pairs Rising, and bring out the best in each other' - so Lantern Pairs Rising is the bold name for the seminar but the point of the whole workshop is in the tagline, 'and bring out the best in each other'.

The final design should compel couples to take the risk to leave their comfort zones and attend a one-day workshop on a weekend .

Target Market(s)

Couples who are interested in self-improvement and identify with change and growth.
Somehow the flyer will match their aspirations!

Requirements
Should not have
• Not too many love hearts! :)
Not too gushy - a hint of romance!

```html
<!DOCTYPE html>
<html lang="en">
<head>
<meta charset="utf-8">
<title>Lantern Pairs Rising – Workshop Flyer</title>
<link href="https://fonts.googleapis.com/css2?family=Arvo:wght@400;700&family=Mulish:wght@300;400;600&family=Raleway:wght@300;400&display=swap" rel="stylesheet">
<style>
  :root {
    --bg: #e6e6e6;
    --cocoa: #4e3c3d;
    --paper: #ffffff;
    --sky: #2bb3e6;
    --blush: #dcb3d5;
    --ink: #3a2c2d;
    --muted: #5a4c4d;
  }
  * { margin: 0; padding: 0; box-sizing: border-box; }
  html, body { width: 1200px; height: 1000px; overflow: hidden; }
  body { background: var(--bg); font-family: "Mulish", sans-serif; position: relative; }

  .spread { position: absolute; left: 67px; top: 70px; width: 1098px; height: 781px; display: flex; }
  .cover { width: 554px; height: 100%; background: var(--cocoa); position: relative; }
  .inside { width: 544px; height: 100%; background: var(--paper); position: relative; }

  .cover-name { position: absolute; left: 48px; top: 290px; font-family: "Raleway", sans-serif; font-weight: 300;
    color: var(--paper); font-size: 70px; line-height: 70px; letter-spacing: -0.5px; white-space: nowrap; }
  .tagline { position: absolute; left: 270px; top: 374px; font-family: "Raleway", sans-serif; font-weight: 300;
    color: var(--paper); font-size: 30px; line-height: 28px; list-style: none; }
  .tagline .pink { color: var(--blush); }
  .tagline .blue { color: var(--sky); }

  .lead { position: absolute; left: 111px; top: 52px; width: 410px; font-family: "Arvo", serif; font-weight: 700;
    color: var(--sky); font-size: 15px; line-height: 17.5px; white-space: nowrap; }
  .gain-title { position: absolute; left: 111px; top: 168px; font-family: "Arvo", serif; font-weight: 700;
    color: var(--ink); font-size: 13px; letter-spacing: 0.2px; white-space: nowrap; }
  .gains { position: absolute; left: 112px; top: 196px; width: 400px; list-style: none; font-size: 11.8px;
    line-height: 13.7px; white-space: nowrap; }
  .gains li { position: relative; padding-left: 12px; color: var(--ink); }
  .gains li::before { content: "•"; position: absolute; left: 0; }
  .gains li:nth-child(even) { color: var(--sky); }

  .presenter-photo { position: absolute; left: 31px; top: 445px; width: 78px; height: 126px;
    background: linear-gradient(180deg, #8fb07a 0%, #b8c9a4 45%, #d9d4cc 100%); }
  .about { position: absolute; left: 122px; top: 441px; width: 390px; font-size: 11px; line-height: 14.2px;
    color: var(--muted); font-weight: 300; white-space: nowrap; }
  .about strong { color: var(--ink); font-weight: 600; }
  .about p + p { margin-top: 14px; }

  .footer-name { position: absolute; left: 118px; top: 596px; font-family: "Raleway", sans-serif; font-weight: 300;
    color: var(--ink); font-size: 46px; line-height: 46px; white-space: nowrap; }
  .cta { position: absolute; left: 122px; top: 698px; font-family: "Arvo", serif; font-weight: 700;
    color: var(--ink); font-size: 12.6px; line-height: 15px; white-space: nowrap; }
  .cta a { color: var(--sky); text-decoration: none; }
</style>
</head>
<body>
  <main class="spread">
    <section class="cover">
      <h1 class="cover-name">Lantern Pairs<br>Rising</h1>
      <ul class="tagline">
        <li>and</li><li>bring</li><li>out</li><li>the</li><li>best</li><li>in</li>
        <li class="pink">each</li><li class="blue">other</li>
      </ul>
    </section>

    <section class="inside">
      <p class="lead">Some couples spend up big on their<br>wedding day but fail to invest in their marriage<br>or relationship, but relationships take much<br>more than love to be successful. This innova-<br>tive one-day seminar helps couples to breathe<br>new life into their relationship.</p>

      <h2 class="gain-title">WHAT YOU WILL GAIN FROM MARTIN’S SEMINAR:</h2>
      <ul class="gains">
        <li>How to turn an argument into a moment of closeness<br>– Easier than you think!</li>
        <li>Know what stress is doing to your relating and the two<br>skillsets will make a big difference to each other’s stress-load.</li>
        <li>The role of pleasure in an emotionally-committed<br>relationship and that’s more than sex!</li>
        <li>Identify the traps of committed relationships – and why being in a<br>relationship doesn’t have to be a struggle.</li>
        <li>Learn how it’s not you or your partner’s fault</li>
        <li>Identify the missing ingredients in your relationship and what you<br>can do to get these back.</li>
        <li>What the research says about the ingredients of great sex</li>
        <li>What to do about the three drains on your relationship:<br>boredom, having nothing to say and those same-old<br>arguments. You will also practice using Martin’s negotiation tool that he<br>developed for couples as well. Martin’s seminars are fun, informative<br>and practical.</li>
      </ul>

      <div class="presenter-photo" role="img" aria-label="Portrait photograph of the presenter outdoors"></div>
      <div class="about">
        <p><strong>About the presenter:</strong> Martin Ashby is a highly skilled couples<br>therapist and educator, who is known for his innovative and creative<br>approaches in his work. He has appeared on the Ch 4’s Morning Desk<br>show and Ch 7’s The Roundup as well as being interviewed on radio<br>and in print.</p>
        <p>Martin’s seminars are run along brain-based education principles that<br>he learnt from Dr Alan Whitcombe’s training in the USA, so that you will<br>remember your new learning and integrate it into your life.</p>
      </div>

      <p class="footer-name">Lantern Pairs<br>Rising</p>
      <p class="cta">Take your relationship to the<br>next level and book your seat now:<br><a href="#">http://www.martinashby.example/couples.html</a></p>
    </section>
  </main>
</body>
</html>
```